Business Card Design Project

it should have the logo in one side
the other side

Name
Position
telephone
email

Target Market(s)

Business prospects and upscale Fashion shoppers

Industry/Entity Type

Business

Font styles to use
Serif
Sans Serif

Requirements
Must have
• very elegant, upscale, modern
Nice to have
• layering, embossed
Should not have
• Should not use any color OTHER THAN black, silver, white or purple

```html
<!DOCTYPE html>
<html lang="en">
<head>
<meta charset="UTF-8">
<title>Velora Luxury Boutique – Business Cards</title>
<link rel="stylesheet" href="https://fonts.googleapis.com/css2?family=Montserrat:wght@300;400;600;700&family=Cinzel:wght@500;700&display=swap">
<style>
  :root {
    --backdrop: #d9d9d9;
    --card-white: #ffffff;
    --ink: #141414;
    --black: #0b0a10;
    --purple: #9a4dff;
    --purple-deep: #6a2fd6;
    --purple-text: #a25cff;
    --shadow: rgba(0, 0, 0, 0.35);
  }
  * { margin: 0; padding: 0; box-sizing: border-box; }
  html, body {
    width: 1200px;
    height: 702px;
    overflow: hidden;
    background: var(--backdrop);
    font-family: "Montserrat", Arial, sans-serif;
  }
  .canvas {
    position: relative;
    width: 1200px;
    height: 702px;
  }
  .card {
    position: absolute;
    overflow: hidden;
    box-shadow: 0 10px 24px var(--shadow);
  }

  /* Contact side */
  .card-front {
    left: 70px;
    top: 40px;
    width: 600px;
    height: 343px;
    background: var(--card-white);
  }
  .feature-panel {
    position: absolute;
    left: 350px;
    top: 0;
    width: 250px;
    height: 325px;
    background: linear-gradient(180deg, var(--black) 0%, var(--purple-deep) 45%, var(--purple) 100%);
  }
  .base-band {
    position: absolute;
    left: 0;
    bottom: 0;
    width: 100%;
    height: 18px;
    background: linear-gradient(90deg, var(--black) 0%, var(--black) 38%, var(--purple) 62%, var(--purple) 100%);
  }
  .brand-small {
    position: absolute;
    left: 42px;
    top: 30px;
    width: 110px;
    text-align: center;
  }
  .brand-small .brand-mark {
    display: block;
    width: 34px;
    height: 34px;
    margin: 0 auto 8px;
    background: linear-gradient(180deg, var(--purple-deep), var(--purple));
  }
  .brand-small .brand-name {
    display: block;
    font-size: 25px;
    font-weight: 400;
    letter-spacing: 1px;
    color: var(--ink);
    line-height: 1;
  }
  .brand-small .brand-tagline {
    display: block;
    margin-top: 4px;
    font-family: "Cinzel", Georgia, serif;
    font-size: 8.5px;
    font-weight: 700;
    letter-spacing: 0.6px;
    color: var(--ink);
  }
  .person {
    position: absolute;
    left: 52px;
    top: 190px;
  }
  .person-name {
    font-size: 17px;
    font-weight: 700;
    color: var(--ink);
    letter-spacing: 0.3px;
  }
  .person-role {
    margin-top: 2px;
    font-size: 9.5px;
    color: var(--purple-text);
    letter-spacing: 0.4px;
  }
  .contact {
    position: absolute;
    left: 52px;
    top: 262px;
    list-style: none;
    font-size: 13px;
    line-height: 19px;
  }
  .contact-label { font-weight: 700; color: var(--ink); }
  .contact-value { color: var(--purple-text); }

  /* Brand side */
  .card-back {
    left: 610px;
    top: 395px;
    width: 508px;
    height: 290px;
    background: linear-gradient(180deg, var(--black) 0%, var(--black) 14%, var(--purple-deep) 52%, var(--purple) 78%, var(--purple) 100%);
  }
  .brand-large {
    position: absolute;
    left: 0;
    top: 92px;
    width: 100%;
    text-align: center;
    color: var(--card-white);
  }
  .brand-large .brand-mark {
    display: block;
    width: 40px;
    height: 40px;
    margin: 0 auto 10px;
    background: var(--card-white);
  }
  .brand-large .brand-name {
    display: block;
    font-size: 32px;
    font-weight: 300;
    letter-spacing: 1.5px;
    line-height: 1;
  }
  .brand-large .brand-tagline {
    display: block;
    margin-top: 5px;
    font-family: "Cinzel", Georgia, serif;
    font-size: 10px;
    font-weight: 500;
    letter-spacing: 1.5px;
  }
</style>
</head>
<body>
<main class="canvas">
  <section class="card card-front" aria-label="Business card, contact side">
    <div class="feature-panel" role="img" aria-label="Large brand monogram decoration in black to purple"></div>
    <div class="base-band"></div>
    <div class="brand-small">
      <span class="brand-mark"></span>
      <span class="brand-name">VELORA</span>
      <span class="brand-tagline">LUXURY BOUTIQUE</span>
    </div>
    <div class="person">
      <p class="person-name">NAME ABCD</p>
      <p class="person-role">DESIGNATION</p>
    </div>
    <ul class="contact">
      <li><span class="contact-label">Tel:</span> <span class="contact-value">555 014 262</span></li>
      <li><span class="contact-label">Email:</span> <span class="contact-value">info@veloraxyz.com</span></li>
      <li><span class="contact-label">Website:</span> <span class="contact-value">www.veloraxyz.com</span></li>
    </ul>
  </section>

  <section class="card card-back" aria-label="Business card, brand side">
    <div class="brand-large">
      <span class="brand-mark"></span>
      <span class="brand-name">VELORA</span>
      <span class="brand-tagline">LUXURY BOUTIQUE</span>
    </div>
  </section>
</main>
</body>
</html>
```